Disruptive Wine Company Business Card

We need a SINGLE-SIDED business card for a wine company that is going to destroy the wine industry as you know it.

The business is meant to be fun, easy, approachable & high tech.

Although the logo is purple & yellow we do not want purple/yellow (bright colored) cards. Maybe a light grey background with the logo on it. Purple or yellow lines/curves in the card design is OK, but it should not be too bright.

These cards will be given out to customers who want to retain the store information or pass the cards along to their friends.

Target Market(s)

young, hip, city dwelling wine lovers

Industry/Entity Type

Industry

Contact Information for Business Card

Looking for a simple but unique design that isn't showy, but will be eye grabbing.

Requirements
Must have
• An eye catching design
Should not have
• Should not be too "showy".

```html
<!DOCTYPE html>
<html lang="en">
<head>
<meta charset="utf-8">
<title>Corkline Wine Company – Business Card</title>
<link href="https://fonts.googleapis.com/css2?family=Lato:wght@300;400;700&display=swap" rel="stylesheet">
<style>
  :root {
    --page-bg: #d9d9db;
    --card-light: #f1f2f4;
    --card-mid: #dcdfe3;
    --purple: #7a3a7c;
    --purple-soft: #ad6bad;
    --gold-top: #d7b844;
    --gold-bottom: #c4902e;
    --ink: #2e2e30;
    --ink-soft: #4a4650;
  }
  html, body {
    margin: 0;
    width: 1200px;
    height: 970px;
    overflow: hidden;
    background: var(--page-bg);
    font-family: "Lato", Arial, sans-serif;
  }
  .stage {
    position: relative;
    width: 1200px;
    height: 970px;
  }
  .business-card {
    position: absolute;
    left: 100px;
    top: 208px;
    width: 856px;
    height: 474px;
    transform: scale(1.1682);
    transform-origin: 0 0;
    background: linear-gradient(160deg, var(--card-light) 0%, var(--card-mid) 100%);
    box-shadow: 0 6px 24px rgba(0,0,0,0.18);
    overflow: hidden;
  }
  .card-waves {
    position: absolute;
    inset: 0;
  }
  .brand {
    position: absolute;
    left: 60px;
    top: 52px;
    color: var(--purple);
    font-weight: 300;
  }
  .brand-mark {
    width: 46px;
    height: 46px;
    background: var(--gold-top);
    margin: 0 0 22px 108px;
  }
  .brand-name {
    font-size: 52px;
    letter-spacing: 6px;
    line-height: 1;
  }
  .brand-tagline {
    font-size: 19px;
    letter-spacing: 4.2px;
    margin-top: 6px;
    padding-left: 6px;
  }
  .person {
    position: absolute;
    right: 43px;
    top: 90px;
    text-align: right;
  }
  .person-name {
    color: var(--purple);
    font-weight: 700;
    font-size: 30px;
    line-height: 1.2;
  }
  .person-title {
    color: var(--ink);
    font-size: 24px;
    line-height: 1.3;
  }
  .contact-list {
    position: absolute;
    left: 52px;
    top: 304px;
    margin: 0;
    padding: 0;
    list-style: none;
  }
  .contact-item {
    display: flex;
    align-items: center;
    height: 33px;
    font-size: 24px;
    color: var(--ink-soft);
  }
  .contact-icon {
    width: 20px;
    height: 20px;
    margin-right: 20px;
    fill: var(--purple);
  }
  .address {
    position: absolute;
    right: 43px;
    top: 320px;
    text-align: right;
    font-size: 24px;
    line-height: 32px;
    color: var(--ink);
  }
  .find-us {
    position: absolute;
    right: 43px;
    top: 404px;
    display: flex;
    align-items: center;
    font-size: 24px;
    color: var(--ink);
  }
  .social-square {
    width: 20px;
    height: 20px;
    border-radius: 3px;
    background: var(--purple);
    margin-left: 12px;
  }
  .social-square:first-of-type { margin-left: 16px; }
</style>
</head>
<body>
<main class="stage">
  <article class="business-card">
    <svg class="card-waves" width="856" height="474" viewBox="0 0 856 474" aria-hidden="true">
      <defs>
        <linearGradient id="goldFill" x1="0" y1="0" x2="0" y2="1">
          <stop offset="0" stop-color="#d7b844"/>
          <stop offset="1" stop-color="#c4902e"/>
        </linearGradient>
      </defs>
      <path d="M0,302 Q428,205 856,300 L856,312 Q428,232 0,312 Z" fill="#ad6bad"/>
      <path d="M0,312 Q428,232 856,312 L856,474 L0,474 Z" fill="url(#goldFill)"/>
    </svg>

    <div class="brand">
      <div class="brand-mark"></div>
      <div class="brand-name">CORKLINE</div>
      <div class="brand-tagline">WINE COMPANY</div>
    </div>

    <div class="person">
      <div class="person-name">Marla Quinn</div>
      <div class="person-title">Director</div>
    </div>

    <ul class="contact-list">
      <li class="contact-item">
        <svg class="contact-icon" viewBox="0 0 20 20" aria-hidden="true"><path d="M2 7c0-3 3-4 8-4s8 1 8 4v2h-4V7H6v2H2z M4 10h12l2 7H2z"/></svg>
        000 222 3344
      </li>
      <li class="contact-item">
        <svg class="contact-icon" viewBox="0 0 20 20" aria-hidden="true"><path d="M6 1h8a2 2 0 0 1 2 2v14a2 2 0 0 1-2 2H6a2 2 0 0 1-2-2V3a2 2 0 0 1 2-2zm0 3v11h8V4zm4 12.2a1 1 0 1 0 0.01 0z"/></svg>
        444 666 7788
      </li>
      <li class="contact-item">
        <svg class="contact-icon" viewBox="0 0 20 20" aria-hidden="true"><path d="M1 4h18v12H1zm2 2v.4l7 5 7-5V6l-7 5z"/></svg>
        hello@corklinewine.com
      </li>
      <li class="contact-item">
        <svg class="contact-icon" viewBox="0 0 20 20" aria-hidden="true"><path d="M10 1a9 9 0 1 0 0 18 9 9 0 0 0 0-18zm0 2c1 1.3 1.8 3 2 6H8c.2-3 1-4.7 2-6zM3.1 9a7 7 0 0 1 3.6-5.2C6.2 5.3 6 7 6 9zm0 2H6c0 2 .2 3.7.7 5.2A7 7 0 0 1 3.1 11zM8 11h4c-.2 3-1 4.7-2 6-1-1.3-1.8-3-2-6zm6 0h2.9a7 7 0 0 1-3.6 5.2c.5-1.5.7-3.2.7-5.2zm0-2c0-2-.2-3.7-.7-5.2A7 7 0 0 1 16.9 9z"/></svg>
        www.corklinewine.com
      </li>
    </ul>

    <div class="address">
      18 Bell St, New York<br>
      NY 10012, USA
    </div>

    <div class="find-us">
      Find Us
      <span class="social-square"></span>
      <span class="social-square"></span>
      <span class="social-square"></span>
    </div>
  </article>
</main>
</body>
</html>
```